harbor lantern security & electric needs a business card

Must be attractive and modern, look professional and upscale!!
We provide alarm and cameras services and 24 hour monitoring for commercial and residential clients. In addition, the owner is a master electrician that provides services to commercial and residential clients.
We also install and service automatic gates. We previously had two different businesses but decided to merge into one, thus creating Harbor Lantern Security & Electric.

Target Market(s)

Commercial Business and residential customers

Industry/Entity Type

Security

Contact Information for Business Card

Front and back design with logo and services listed

Font styles to use
Sans Serif

Colors
ec1f27
0355a3
fbee3f

Requirements
Must have
• Front of card:
• Marcus Tremblow-Owner
• telephone icon and then the number 936-555-0193
• Mail icon and then email address mtremblow@quillmail.example
• World Icon then website www.yourharborlanterntx.example
• Location marker and then Marrowfield, Texas
• We would like to have a picture of the logo at least on the front
• Also need motto on front: We're There When You're Not
• The front of the card must also say Licensed and Insured in addition to:
• License Number: K47315
• TECL: 58629
• On the Back of the Card:
• List each of these Services with check marks:
• Residential and Commercial Electrical Services
• Electric Gates
• Alarm Systems
• Alarm Monitoring
• Cameras
• ***Use separate attached logo, the business card design is just to be used as a model***
Nice to have
• It would be nice to have the logo on back of the card in addition to these words at the bottom:
• "No job too big or small, we do it all!"
Should not have
• Anything crazy!!

```html
<!DOCTYPE html>
<html lang="en">
<head>
<meta charset="utf-8">
<title>Harbor Lantern Security &amp; Electric – Business Card</title>
<link href="https://fonts.googleapis.com/css2?family=Exo+2:ital,wght@0,400;0,600;0,700;1,400&display=swap" rel="stylesheet">
<style>
  :root {
    --page-bg: #d9d6d2;
    --card-light: #f1f2f4;
    --card-light-edge: #dfe2e6;
    --brand-red: #ec1f27;
    --brand-red-deep: #b3121a;
    --brand-navy: #1c2140;
    --edge-grey: #b9bcc4;
    --text-on-red: #ffffff;
    --service-text: #f7c9cb;
    --text-dark: #2b2d35;
  }
  * { margin: 0; padding: 0; box-sizing: border-box; }
  html, body {
    width: 1200px; height: 969px; overflow: hidden;
    background: var(--page-bg);
    font-family: "Exo 2", sans-serif;
  }
  .canvas { position: relative; width: 1200px; height: 969px; }
  .card {
    position: absolute; left: 100px; top: 200px;
    width: 1000px; height: 570px;
    background: linear-gradient(135deg, var(--card-light), var(--card-light-edge));
    overflow: hidden;
    box-shadow: 0 18px 40px rgba(0,0,0,.22);
  }
  .card-shape { position: absolute; inset: 0; }
  .brand {
    position: absolute; left: 40px; width: 400px; top: 50px;
    text-align: center;
  }
  .brand-mark {
    width: 110px; height: 110px; border-radius: 50%;
    background: var(--brand-red); margin: 0 auto 18px;
  }
  .brand-name {
    color: var(--brand-navy); font-weight: 700;
    font-size: 34px; line-height: 1.05; letter-spacing: .3px;
  }
  .owner-name {
    margin-top: 26px; color: var(--brand-red);
    font-weight: 700; font-size: 31px;
  }
  .owner-title { margin-top: 6px; color: var(--text-dark); font-size: 25px; }

  .details {
    position: absolute; right: 38px; top: 52px;
    text-align: right; color: var(--text-on-red);
  }
  .contact-line {
    display: flex; justify-content: flex-end; align-items: center;
    gap: 12px; font-size: 24px; height: 38px;
  }
  .contact-line svg { width: 22px; height: 22px; fill: var(--text-on-red); }
  .license { margin-top: 8px; font-size: 25px; line-height: 38px; }
  .motto { margin-top: 18px; font-style: italic; font-size: 27px; }
  .services-heading { margin-top: 22px; font-weight: 600; font-size: 29px; }
  .service-list {
    margin-top: 6px; font-style: italic; font-size: 23px;
    color: var(--service-text); line-height: 35px; list-style: none;
  }
  .dot {
    display: inline-block; width: 9px; height: 9px; border-radius: 50%;
    background: var(--text-on-red); margin: 0 8px 3px; vertical-align: middle;
  }
</style>
</head>
<body>
<main class="canvas">
  <article class="card">
    <svg class="card-shape" viewBox="0 0 1000 570" width="1000" height="570" aria-hidden="true">
      <defs>
        <linearGradient id="redPanel" x1="0" y1="0" x2="1" y2="1">
          <stop offset="0" stop-color="#ec1f27"/>
          <stop offset="1" stop-color="#b3121a"/>
        </linearGradient>
      </defs>
      <path d="M395 0 L585 118 C565 330 420 490 200 570 L1000 570 L1000 0 Z" fill="url(#redPanel)"/>
      <path d="M372 0 L568 122 C548 328 400 488 178 570" fill="none" stroke="#b9bcc4" stroke-width="4"/>
      <path d="M385 0 L578 120 C558 330 412 490 190 570" fill="none" stroke="#1c2140" stroke-width="16"/>
    </svg>

    <section class="brand">
      <div class="brand-mark"></div>
      <h1 class="brand-name">Harbor Lantern<br>Security &amp; Electric</h1>
      <p class="owner-name">Marcus Tremblow-Owner</p>
      <p class="owner-title">CEO/Founder</p>
    </section>

    <section class="details">
      <p class="contact-line">Pin icon Marrowfield, Texas</p>
      <p class="contact-line">936-555-0193
        <svg viewBox="0 0 24 24"><path d="M6.6 10.8a15 15 0 0 0 6.6 6.6l2.2-2.2a1 1 0 0 1 1-.25 11.4 11.4 0 0 0 3.6.57 1 1 0 0 1 1 1V20a1 1 0 0 1-1 1A17 17 0 0 1 3 4a1 1 0 0 1 1-1h3.5a1 1 0 0 1 1 1c0 1.25.2 2.45.57 3.6a1 1 0 0 1-.25 1z"/></svg></p>
      <p class="contact-line">mtremblow@quillmail.example
        <svg viewBox="0 0 24 24"><path d="M3 5h18v14H3zm2 2v.4l7 4.6 7-4.6V7zm0 2.8V17h14V9.8l-7 4.6z"/></svg></p>
      <p class="contact-line">yourharborlanterntx.example
        <svg viewBox="0 0 24 24"><path d="M12 2a10 10 0 1 0 0 20 10 10 0 0 0 0-20zm6.9 6h-2.9a15 15 0 0 0-1.4-3.6A8 8 0 0 1 18.9 8zM12 4c.8 1.2 1.5 2.5 1.9 4h-3.8c.4-1.5 1.1-2.8 1.9-4zM4.3 14a8 8 0 0 1 0-4h3.4a16 16 0 0 0 0 4zm.8 2h2.9a15 15 0 0 0 1.4 3.6A8 8 0 0 1 5.1 16zM8 8H5.1a8 8 0 0 1 4.3-3.6A15 15 0 0 0 8 8zm4 12c-.8-1.2-1.5-2.5-1.9-4h3.8c-.4 1.5-1.1 2.8-1.9 4zm2.3-6H9.7a14 14 0 0 1 0-4h4.6a14 14 0 0 1 0 4zm.3 5.6A15 15 0 0 0 16 16h2.9a8 8 0 0 1-4.3 3.6zM16.3 14a16 16 0 0 0 0-4h3.4a8 8 0 0 1 0 4z"/></svg></p>
      <p class="license">Licensed &amp; Insured<br>Lic No: K47315 | TECL: 58629</p>
      <p class="motto">We’re There When You’re Not</p>
      <h2 class="services-heading">CHECK MARKS</h2>
      <ul class="service-list">
        <li>Electric Gates<span class="dot"></span>Alarm Systems</li>
        <li>Alarm Monitoring<span class="dot"></span>Cameras</li>
        <li>Residential &amp; Commercial Electrical Services</li>
      </ul>
    </section>
  </article>
</main>
</body>
</html>
```